Redesign of QuillLexicon.com in Bootstrap 4

Current design of QuillLexicon.com is not responsive. We need to change it to latest version of Bootstrap 4 keeping essential elements in place.

Apart from home page, we need designs for http://www.quilllexicon.com/meaning/cat also.

Coding

Coded - Design and coding required

Number of Pages Required

2 page

Colors
34a7d8

Requirements
Must have
• Bootstrap 4

```html
<!DOCTYPE html>
<html lang="en">
<head>
<meta charset="utf-8">
<title>Quill Lexicon – Home</title>
<link href="https://fonts.googleapis.com/css2?family=Raleway:wght@400;500;600;700;800&display=swap" rel="stylesheet">
<style>
:root{
  --orange:#f7941d;
  --blue:#0d6db7;
  --blue-text:#1277c2;
  --dark:#2b2b2b;
  --darker:#1f1f1f;
  --text:#444;
  --muted:#666;
  --border:#cfe0ee;
  --card-bg:#f3f8fc;
}
*{box-sizing:border-box;margin:0;padding:0}
html,body{width:873px;height:1200px;overflow:hidden}
body{font-family:'Raleway',sans-serif;color:var(--text);background:#fff;position:relative}
.abs{position:absolute}
a{color:inherit;text-decoration:none}

/* header */
.site-header{left:0;top:0;width:873px;height:60px;background:linear-gradient(#fff,#eef4f9);border-bottom:1px solid #dde6ee}
.brand{left:108px;top:12px;display:flex;align-items:center;gap:6px}
.brand-mark{width:12px;height:12px;background:var(--orange)}
.brand-name{font-size:15px;font-weight:800;color:var(--blue-text);line-height:1}
.main-nav{left:241px;top:0;display:flex;height:60px;align-items:center;font-size:9px;font-weight:600;color:#555}
.main-nav a{padding:0 15px;border-right:1px solid #ccc;line-height:12px}
.main-nav a:last-child{border:0}
.main-nav .active{background:var(--orange);color:#fff;height:60px;line-height:60px;width:49px;padding:0;text-align:center;border:0;margin-right:12px}
.join-btn{left:694px;top:23px;width:70px;height:19px;background:var(--dark);color:#fff;font-size:8.5px;font-weight:700;text-align:center;line-height:19px;border:1px solid #000}

/* hero */
.hero{left:0;top:60px;width:873px;height:328px;background:linear-gradient(100deg,#8fbb1a 0%,#cfe65a 30%,#f2f197 52%,#e9dfae 75%,#d0a56b 100%)}
.hero-title{left:109px;top:102px;font-size:18px;font-weight:700;color:#1b1b1b}
.hero-list{left:109px;top:133px;list-style:none;font-size:10.5px;color:#222;width:290px}
.hero-list li{display:flex;gap:5px;margin-bottom:10.5px;line-height:14px}
.hero-list svg{flex:none;margin-top:2px}
.hero-list .free{color:var(--blue-text);font-weight:700;text-decoration:underline}

/* search band */
.search-band{left:0;top:388px;width:873px;height:60px;background:var(--blue)}
.search-title{left:109px;top:406px;font-size:17px;font-weight:700;color:#fff}
.search-input{left:333px;top:404px;width:318px;height:30px;background:#fff;border:1px solid #ccd;font-size:10.5px;color:#999;padding-left:9px;line-height:28px}
.search-btn{left:670px;top:404px;width:93px;height:30px;background:var(--orange);color:#111;font-weight:700;font-size:11px;text-align:center;line-height:30px}

/* ad banner */
.ad-banner{left:126px;top:465px;width:396px;height:48px;border:1px solid #333;background:#fff}
.ad-dot{left:10px;top:13px;width:20px;height:20px;border-radius:50%;background:var(--blue)}
.ad-head{left:42px;top:6px;font-size:9px;font-weight:700;color:#111}
.ad-sub{left:42px;top:21px;font-size:6.8px;font-weight:700;color:#111;line-height:9.5px}
.ad-cta{left:252px;top:16px;width:66px;height:14px;background:#d9371f;color:#fff;font-size:7px;font-weight:700;text-align:center;line-height:14px}
.ad-art{left:322px;top:0;width:73px;height:46px;background:linear-gradient(120deg,#123b7a,#2769b8,#0f1f3d)}

/* feature cards */
.card{left:109px;width:430px;background:linear-gradient(#eaf2f9,#fff 60%);border:1px solid var(--border);border-radius:2px}
.thumb{left:124px;width:81px;height:82px;background:#fff;border:1px solid #8ab3d6;box-shadow:0 1px 2px rgba(0,0,0,.15)}
.thumb-word{font-size:9.5px;color:#444;text-align:center;line-height:80px}
.thumb-fill{position:absolute;inset:3px}
.card-title{left:219px;font-size:17px;color:var(--blue-text);font-weight:400}
.card-text{left:219px;width:312px;font-size:8.5px;line-height:13.2px;color:#555}
.card-btn{left:219px;width:72px;height:20px;background:var(--orange);color:#fff;font-size:8.5px;font-weight:600;text-align:center;line-height:20px;border-bottom:2px solid #d77a0c}

/* browse */
.browse-label{left:114px;top:992px;font-size:8.5px;font-weight:700;color:#333}
.alpha-box{left:109px;top:1010px;width:430px;height:31px;border:1px solid var(--border);background:var(--card-bg);display:flex;gap:2px;padding:8px 0 0 8px}
.alpha-box span{width:14px;height:12px;border:1px solid #bbb;background:#fff;font-size:6.5px;text-align:center;line-height:11px;color:#555}
.alpha-box span.on{border-color:var(--orange);color:var(--orange)}

/* sidebar */
.sidebar{left:557px;top:465px;width:206px;height:576px;border:1px solid var(--border);background:#f5f9fc}
.panel-head{left:568px;width:184px;height:24px;font-size:11px;font-weight:600;color:#fff;padding-left:12px;line-height:24px}
.login-box{left:568px;top:476px;width:184px;height:108px;background:#fff;border:1px solid #ddd}
.field{left:574px;width:172px;height:20px;border:1px solid #d4d4d4;background:#f6f6f6;font-size:8.5px;color:#555;padding-left:7px;line-height:18px}
.login-btn{left:574px;top:562px;width:64px;height:21px;background:var(--blue);color:#fff;font-weight:700;font-size:10.5px;text-align:center;line-height:21px}
.forgot{left:647px;top:567px;font-size:8px;color:var(--orange);text-decoration:underline}
.wotd{left:568px;top:600px;width:184px;height:110px;background:#fff;border:1px solid #ddd}
.wotd-word{left:580px;top:638px;font-size:11px;color:#333}
.wotd-phon{left:582px;top:664px;font-size:8px;color:#777}
.audio{left:724px;top:639px;width:17px;height:17px;border-radius:50%;background:#dfe7ee}
.wotd-foot{left:568px;top:688px;width:184px;height:22px;background:#eef1f4;border-top:1px solid #ddd}
.social{top:694px;width:12px;height:12px}
.show-def{left:669px;top:692px;width:80px;height:16px;background:var(--blue);color:#fff;font-size:8px;font-weight:700;text-align:center;line-height:16px}
.side-ad{left:582px;top:724px;width:156px;height:129px;background:linear-gradient(160deg,#3c4247,#23272a 70%,#4a4a3a)}
.side-ad-title{left:591px;top:735px;font-size:13px;font-weight:800;color:#fff;letter-spacing:.3px}
.side-ad-sub{left:592px;top:753px;font-size:6.8px;color:#eee;line-height:8.5px;letter-spacing:.5px}
.side-ad-more{left:592px;top:790px;font-size:6.8px;font-weight:700;color:var(--orange)}

/* footer */
.site-footer{left:0;top:1060px;width:873px;height:118px;background:var(--dark);border-top:3px solid var(--orange)}
.foot-col{top:1077px;width:130px;color:#ddd}
.foot-col h4{font-size:9.5px;font-weight:700;color:#fff;padding-bottom:8px;border-bottom:1px solid #555;margin-bottom:8px}
.foot-col ul{list-style:disc;padding-left:10px;font-size:8px;line-height:16.5px}
.foot-divider{top:1077px;width:1px;height:80px;background:#444}
.foot-brand{left:620px;top:1088px;width:140px;text-align:center}
.foot-brand .name{font-size:16px;font-weight:800;color:#999}
.foot-brand .tag1{font-size:7.3px;font-weight:700;color:#fff;margin-top:10px}
.foot-brand .tag2{font-size:7.3px;color:#ddd;line-height:10.5px}
.foot-tagline{left:108px;top:1159px;font-size:10.5px;color:var(--orange)}
.copyright-bar{left:0;top:1178px;width:873px;height:22px;background:var(--darker);font-size:8px;color:#ccc;padding-left:110px;line-height:22px}
</style>
</head>
<body>

<header class="abs site-header">
  <a class="abs brand" href="#"><span class="brand-mark"></span><span class="brand-name">Quill Lexicon</span></a>
  <nav class="abs main-nav">
    <a class="active" href="#">Home</a>
    <a href="#">Idioms</a>
    <a href="#">Crossword</a>
    <a href="#">Comman Errors</a>
    <a href="#">Blog</a>
    <a href="#">Contact</a>
  </nav>
  <a class="abs join-btn" href="#">Join For FREE</a>
</header>

<section class="abs hero" role="img" aria-label="Open book with fanned pages on a bright green background"></section>
<h1 class="abs hero-title">Search, Save and Master Words</h1>
<ul class="abs hero-list">
  <li><svg width="11" height="11" viewBox="0 0 11 11"><rect x="0.7" y="1.7" width="8.5" height="8.5" fill="none" stroke="#222" stroke-width="1.3"/><path d="M2.5 5.5l2 2L10 1" fill="none" stroke="#222" stroke-width="1.6"/></svg>Search From More Than 300,000 Words And Phrases</li>
  <li><svg width="11" height="11" viewBox="0 0 11 11"><rect x="0.7" y="1.7" width="8.5" height="8.5" fill="none" stroke="#222" stroke-width="1.3"/><path d="M2.5 5.5l2 2L10 1" fill="none" stroke="#222" stroke-width="1.6"/></svg>Multiple Usages To Clarify The Context</li>
  <li><svg width="11" height="11" viewBox="0 0 11 11"><rect x="0.7" y="1.7" width="8.5" height="8.5" fill="none" stroke="#222" stroke-width="1.3"/><path d="M2.5 5.5l2 2L10 1" fill="none" stroke="#222" stroke-width="1.6"/></svg>Audio, Phonetics, Meanings, Synonyms And Antonyms</li>
  <li><svg width="11" height="11" viewBox="0 0 11 11"><rect x="0.7" y="1.7" width="8.5" height="8.5" fill="none" stroke="#222" stroke-width="1.3"/><path d="M2.5 5.5l2 2L10 1" fill="none" stroke="#222" stroke-width="1.6"/></svg>Save The Words To Your Personal Deck And Access From Anywhere</li>
  <li><svg width="11" height="11" viewBox="0 0 11 11"><rect x="0.7" y="1.7" width="8.5" height="8.5" fill="none" stroke="#222" stroke-width="1.3"/><path d="M2.5 5.5l2 2L10 1" fill="none" stroke="#222" stroke-width="1.6"/></svg><span>It's <a class="free" href="#">Free</a></span></li>
</ul>

<section class="abs search-band"></section>
<h2 class="abs search-title">Quill English Dictionary</h2>
<div class="abs search-input">Enter the word</div>
<div class="abs search-btn">Search</div>

<aside class="abs ad-banner">
  <span class="abs ad-dot"></span>
  <div class="abs ad-head">Printer data breach?</div>
  <div class="abs ad-sub">Defend your network with our most secure printers.<br>Download the #secureprinting guidance.</div>
  <div class="abs ad-cta">Find out more</div>
  <div class="abs ad-art" role="img" aria-label="Blue digital data graphic"></div>
</aside>

<div class="abs card" style="top:535px;height:86px"></div>
<div class="abs thumb" style="top:526px"><div class="thumb-word">gibe/jibe</div></div>
<h3 class="abs card-title" style="top:541px">English Tidbit</h3>
<p class="abs card-text" style="top:567px">To 'gibe' is to taunt. Gibe is however slowly going out of use. Jibe means to agree but is often used in the negative sense. Although the versions of the tricksters jibed, the police</p>

<div class="abs card" style="top:651px;height:86px"></div>
<div class="abs thumb" style="top:642px"><div class="thumb-fill" role="img" aria-label="Crossword grid with a pen nib" style="background:linear-gradient(135deg,#d9d9d9,#8c8c8c)"></div></div>
<h3 class="abs card-title" style="top:657px">Daily Crossword</h3>
<p class="abs card-text" style="top:683px">Take this daily crossword challenge from Quill Lexicon.</p>
<a class="abs card-btn" style="top:700px" href="#">Solve Now</a>

<div class="abs card" style="top:767px;height:91px"></div>
<div class="abs thumb" style="top:758px"><div class="thumb-fill" role="img" aria-label="Screenshot of the dictionary browser add-on popup" style="background:linear-gradient(#e7eef7,#f8fbfd)"></div></div>
<h3 class="abs card-title" style="top:773px">Foxglide Addon</h3>
<p class="abs card-text" style="top:799px">Add this tool to your Foxglide and quickly look up for definitions from any website without leaving the page.</p>
<a class="abs card-btn" style="top:831px" href="#">Get it Now</a>

<div class="abs card" style="top:890px;height:86px"></div>
<div class="abs thumb" style="top:881px"><div class="thumb-fill" role="img" aria-label="Smartphone showing the dictionary app" style="background:linear-gradient(90deg,#fff 30%,#555 40%,#ccc 50%,#555 60%,#fff 70%)"></div></div>
<h3 class="abs card-title" style="top:896px">Designed for Pocketphone</h3>
<p class="abs card-text" style="top:921px">Quill Lexicon is specially designed for your Pocketphone to quickly lookup meaining, usages and audio of words.</p>

<div class="abs browse-label">Browse Dictionary</div>
<div class="abs alpha-box">
  <span class="on">A</span><span>B</span><span>C</span><span>D</span><span>E</span><span>F</span><span>G</span><span>H</span><span>I</span><span>J</span><span>K</span><span>L</span><span>M</span><span>N</span><span>O</span><span>P</span><span>Q</span><span>R</span><span>S</span><span>T</span><span>U</span><span>V</span><span>W</span><span>Y</span><span>X</span><span>Z</span>
</div>

<aside class="abs sidebar"></aside>
<div class="abs login-box"></div>
<div class="abs panel-head" style="top:476px;background:var(--orange)">Login</div>
<div class="abs field" style="top:507px">Username</div>
<div class="abs field" style="top:534px">Password</div>
<div class="abs login-btn">Login</div>
<a class="abs forgot" href="#">Forgot Password?</a>

<div class="abs wotd"></div>
<div class="abs panel-head" style="top:600px;background:var(--dark)">Word of the Day</div>
<div class="abs wotd-word">Ascendancy</div>
<div class="abs wotd-phon">/ From the sen si /</div>
<div class="abs audio"><svg width="17" height="17" viewBox="0 0 17 17"><path d="M5 7h2l3-2.5v8L7 10H5z" fill="var(--blue)"/><path d="M11.5 6.5q1.5 2 0 4" stroke="var(--blue)" fill="none"/></svg></div>
<div class="abs wotd-foot"></div>
<span class="abs social" style="left:580px;background:#29a8e0"></span>
<span class="abs social" style="left:597px;background:#f26522"></span>
<div class="abs show-def">Show Definition</div>

<div class="abs side-ad" role="img" aria-label="Boy in a suit reading a large book at a desk"></div>
<div class="abs side-ad-title">SHOP TALK</div>
<div class="abs side-ad-sub">WEEKLY NEWS,<br>INSIGHT, AND<br>INSPIRATION.</div>
<div class="abs side-ad-more">READ MORE&gt;</div>

<footer class="abs site-footer"></footer>
<div class="abs foot-col" style="left:110px"><h4>Quilllexicon</h4><ul><li>FAQ</li><li>Contact</li><li>Blog</li></ul></div>
<div class="abs foot-divider" style="left:261px"></div>
<div class="abs foot-col" style="left:278px"><h4>Legal</h4><ul><li>Privacy Policy</li><li>Terms of Use</li></ul></div>
<div class="abs foot-divider" style="left:430px"></div>
<div class="abs foot-col" style="left:446px"><h4>Others</h4><ul><li>Popular Words</li><li>Common Errors in English</li><li>Exam Prep Online</li></ul></div>
<div class="abs foot-divider" style="left:596px"></div>
<div class="abs foot-brand">
  <div class="name">Quill Lexicon</div>
  <div class="tag1">Quill Lexicon Dictionary:</div>
  <div class="tag2">Meaning/Definition, Audio, Phonetics,<br>Usages and more</div>
</div>
<div class="abs foot-tagline">Quill Lexicon Dictionary: Meaning/Definition, Audio, Phonetics, Usages and more</div>
<div class="abs copyright-bar">Copyright © 2016 Lexora Solutions Pvt. Ltd. All rights reserved.</div>

</body>
</html>
```